Single Side Postcard Size Flyer Design

We want to design an attractive and eye-catching sign for hair stylists and barbers to sit on their workstations to attract the attention of their clients regarding hair loss and encourage them to speak to their stylist about it of they are would like to seek treatment.
Many men and women suffer from hair loss, but are often in denial it is happening or too embarrassed to talk about it.
This postcard sized flyer is designed to stick to the mirror at their hair stylist or barber and encourage them to ask their stylist about it.
We want this to be very plain and simple. With just perhaps some kind of simple head line and worry lines. I have uploaded a simple idea.
I have also uploaded the print templates that must be used to provide final designs.

Target Market(s)

Men aged 25 to 60 with thinning hair

Industry/Entity Type

Healthcare

Font styles to use
Sans Serif

Colors
0355a3
ffffff
cfcfcf
1b1b1b

Requirements
Must have
• Flyer size is vertical 4" x 6"
• Copy for the flyer is as follows ans is in color blue: #014ca5
• Worried About Thinning Hair?
• 2 out of 3 Men will have visible hair loss by age 35.
• The Good News is that your
• Barber or Stylist can tell you how to
• stop the loss & grow back your hair.
• Just ask.
• The Brisk Lattice Program from
• The Marlow Pine Company
• New Science. No Surgery. Your Hair.
• www.quellvantinfo.example
Should not have
• - dont add any logos, images or ornate design. this needs to be simple, easy to ready and eye catching.
• - do not use the color red in any capacity.

```html
<!DOCTYPE html>
<html lang="en">
<head>
<meta charset="utf-8">
<title>Worried About Thinning Hair? – Stylist Mirror Card</title>
<link rel="stylesheet" href="https://fonts.googleapis.com/css2?family=Roboto:wght@400;500;700;900&display=swap">
<style>
  :root {
    --brand-blue: #014ca5;
    --box-blue: #0355a3;
    --paper: #ffffff;
    --soft-grey: #cfcfcf;
    --ink: #1b1b1b;
  }
  * { margin: 0; padding: 0; box-sizing: border-box; }
  html, body {
    width: 800px;
    height: 1200px;
    overflow: hidden;
    background: var(--paper);
    font-family: "Roboto", Arial, sans-serif;
  }
  .card {
    position: relative;
    width: 800px;
    height: 1200px;
    background: var(--paper);
    border: 6px solid var(--soft-grey);
  }
  .accent-bar {
    position: absolute;
    left: 67px;
    top: 56px;
    width: 100px;
    height: 494px;
    background: var(--ink);
  }
  .headline {
    position: absolute;
    left: 184px;
    top: 56px;
    display: flex;
    flex-direction: column;
    align-items: flex-start;
    gap: 16px;
  }
  .headline-word {
    display: block;
    font-weight: 700;
    font-size: 84px;
    line-height: 108px;
    height: 108px;
    padding: 0 16px 0 12px;
    color: var(--paper);
    background: var(--box-blue);
    letter-spacing: -0.5px;
  }
  .headline-word--muted {
    font-weight: 400;
    color: var(--ink);
    background: var(--soft-grey);
    padding-right: 60px;
  }
  .message {
    position: absolute;
    right: 50px;
    top: 600px;
    width: 640px;
    text-align: right;
    color: var(--ink);
  }
  .stat-lead {
    font-weight: 700;
    font-size: 38px;
    line-height: 44px;
    color: var(--brand-blue);
  }
  .stat-detail {
    font-size: 27px;
    line-height: 34px;
    margin-bottom: 18px;
  }
  .good-news {
    font-size: 27px;
    line-height: 35px;
    margin-bottom: 8px;
  }
  .call-to-action {
    font-weight: 700;
    font-size: 92px;
    line-height: 100px;
    color: var(--brand-blue);
    letter-spacing: -1px;
  }
  .program {
    font-size: 27px;
    line-height: 34px;
    margin-top: 4px;
  }
  .tagline {
    font-weight: 700;
    font-size: 35px;
    line-height: 44px;
    color: var(--brand-blue);
    margin-top: 6px;
  }
  .web-address {
    font-size: 25px;
    line-height: 32px;
  }
</style>
</head>
<body>
  <main class="card">
    <div class="accent-bar" aria-hidden="true"></div>
    <h1 class="headline">
      <span class="headline-word">Worried</span>
      <span class="headline-word">About</span>
      <span class="headline-word headline-word--muted">Thinning</span>
      <span class="headline-word">Hair?</span>
    </h1>
    <section class="message">
      <p class="stat-lead">2 out of 3 Men</p>
      <p class="stat-detail">will have visible hair<br>loss by age 35.</p>
      <p class="good-news">The Good News is that your Barber<br>or Stylist can tell you how to stop<br>the loss &amp; grow back your hair.</p>
      <p class="call-to-action">Just ask.</p>
      <p class="program">The Brisk Lattice Program<br>from The Marlow Pine Company</p>
      <p class="tagline">New Science. No Surgery. Your Hair.</p>
      <p class="web-address">www.quellvantinfo.example</p>
    </section>
  </main>
</body>
</html>
```